Leading the way in online fitness and education requires power house web design

If you need to contact me you can do so via
skype: Travlin

We need a website designed for new company based in Houston Texas called "TravlinFit". We offer web based training and nutrition programs for our members for example we use the same software as these companies: http://marobelka.com/ http://www.liftquorra.com/ i would like my visitors to be captivated by the level of design creativity of the site.

colors to use would be grey, orange and green.
for example i like the green of this site http://www.cartbeam.com/
i will upload my logo files so you can get a feel for shades of grey and orange.

there is a 3d effect filter i would like applied to my logo for use in the web design i have uploaded what that effect looks like.

i will need your designs to be complete with all interior pages which will include Home, Fitness, Nutrition, Fit Lounge, Fit Score, Fit School, Contact Us, Sign up.

fit lounge on my site is the same as pathwick on liftquorra and locker room on marobelka just re branded.

fit school is a research corner for members to learn about health and fitness, we are members of major medical journals on health and fitness and will have all our articles be from the newest research findings.

competitor sites
these sites use same software:
http://marobelka.com/
http://www.liftquorra.com/

these sites are other software.
http://home.sprintmesa.com/software-for-athletes.aspx
http://www.vigordex.com/

here are some websites that i like:
http://www.crestwaveplay.com/
http://www.nub-lantern.com/
http://fimzol.com/
http://www.parqudo.com/
http://www.lortavi.de/fandiloop/
http://brisketmade.com/

i also like the greens in this site that i am uploading

I have been reviewing the designs and would like to update everyone at once I do not want a normal fitness website design style, no testimonials, blog post, bodyfat calculator

my website will be a membership based website. i want the website to sell the main points of my fitness app that my members will have access to look at the comments for my selling points, use those points in the site create designs and graphics to visualize those points.

look at these sites and gain inspiration

http://www.tuvelo.com.pl/#/projekty/case-studies
http://www.quendar.com/en#/home#ld-kpvm-402617-0045
http://www.nub-lantern.com/
http://fimzol.com/
http://www.parqudo.com/

i have a few designers asking me what the selling points are, the website needs to be built around these points

main selling points.

overview

programs utilize the best multi-joint exercises combined with high intensity cardio, to give you a full-body workout, efficiently and effectively. This means you’re burning more calories and building more lean muscle per unit of time than traditional weight training and cardio programs.

When you sign up, you''ll receive a work out and diet plan to fit your goals and fitness level. As you progress through your plan, you can use the personal fitness and meal calendar to record your results. When you sign-up we''ll ask you a series of questions and your workouts will be tailored to your exact needs. That means never having to use a generic diet and exercise plan again.

If you''ve ever tried to lose weight and build muscle and didn''t succeed, we feel your pain. Until now, trying to navigate all the fitness fads and latest trends on your own has been difficult. The best option - hiring a certified personal trainer - may be out of your financial reach. That''s where we come in - we''re personal trainers on a mission to help you reach your fitness goals quickly and for less money than in person training. Best of all, we''re here to help you day or night.

Fitness

Personal Fitness Calendar

Tailored to the member’s schedule and flexible to accommodate any changes to a member’s regular fitness schedule. Track your progress and stay on track with your fitness goals.

Custom Fitness Plan

Based on a member’s current physical condition and goals.

• Step by step exercise instructions
• 3-D video demonstrations of over 600 exercises, including functional and body-weight only movements
• Equipment filter can customize plans to your gym’s equipment package
• Record workouts to track exercise history and progression

Nutrition

Nutritional Assessment

Daily recommended caloric intake (Protein, Carbohydrates and Fats), based on personal profile and daily fitness plan.

Custom Meal Plan

Personalized meal plan based on nutritional assessment.

• Choose number of meals per day
• Add dietary restrictions, food preferences or dislikes
• Database of thousands of ingredients allows for hundreds of thousands of meal combinations
• Include favorite foods by entering custom nutritional information

Weight tracking

Calculate goal weight and track weight-loss or weight-gain progress. You will reach your goals in no time.

Fit Lounge

What is the most important part of any workout or fitness program? Staying motivated. And what better form of motivation than positive encouragement from your peers?

Fit Lounge is fitness focused social network for health-minded individuals looking for a simple and convenient place to track their workout goals and monitor their progress. A unique system of motivation, support and accountability makes setting fitness goals and then keeping up with them easy

Track

Start by setting fitness goals that you want to track. They can be anything from running and jogging to how many hours of sleep you are getting and how many glasses of water you are drinking every day. Other members of the travlinfits community might be tracking the same workout goals as you, so you can always join their groups as well.

Share

Once you start tracking your workout goals, you can share your progress with your friends. Reach a new max on your bench press? Let everyone know. Eclipse the 10 mile mark on your daily run? Spread the word! The communication of encouragement back and forth is a great way to ensure that everyone stays on track with their workout goals.

Achieve

Of course, the point of any workout or fitness program is to achieve the goals you’ve set. And with help from travlinfits workout tracking tools and encouragement from the community, you will achieve your workout goals in no time. When you see a friend has achieved his or her fitness goals, you can send them a virtual “fist bump” as a sign of congratulations. The number of “fist bumps” each user accumulates will be displayed on their profile, providing additional motivation and a healthy dose of competition.

Reason: i dont feel the designs i have received are of the quality i am looking for

check this website out, i know its flash, but i also know you can get creative without flash and have nice effects throughout the site.

http://www.driftlane-hub.com/

I dont want plain jane designs, insert the content i provided into the site and have it explored in a unique way. take as much time on the design as you need as i will keep extending deadline until i find one that is perfect.

as said before don't make the site anything like the competition sites, its only purpose is to sell the memberships using content provided so i need an innovative way to for them to explore that content,

as your designing this site add me on skype so i can detail and help brainstorm ideas my skype id is travlin
you can stray from the color scheme a little or throw it away if you want i just want to see how creative you can get.

Industry/Entity Type

School

Requirements
Nice to have
• if you notice at the bottom of http://marobelka.com/ she has the orange bar with the three short content parts, i like the idea of having a space like that for similar content.

on http://www.vigordex.com/ if you look to the left side of the scrolling icons i like the idea of having icons or animated pictures to point of key benefits.

```html
<!DOCTYPE html>
<html lang="en">
<head>
<meta charset="utf-8">
<title>TravlinFit — Personal Training</title>
<link rel="stylesheet" href="https://fonts.googleapis.com/css2?family=Source+Sans+3:wght@400;600;700&display=swap">
<style>
  :root {
    --green-deep: #3a7416;
    --green-mid: #4f9a1f;
    --green-glow: #66c42c;
    --green-accent: #7fd42b;
    --orange: #f05a0e;
    --orange-dark: #cf3f05;
    --orange-light: #ff7a2a;
    --ink: #2f3335;
    --ink-soft: #3b3b3b;
    --grey-band: #e1e1e1;
    --white: #ffffff;
    --footer: #2e3537;
    --card-border: rgba(255,255,255,0.55);
  }
  * { box-sizing: border-box; margin: 0; padding: 0; }
  html, body { width: 1132px; height: 1200px; overflow: hidden; }
  body {
    font-family: "Source Sans 3", "Myriad Pro", Arial, sans-serif;
    color: var(--ink-soft);
    background: var(--white);
    position: relative;
  }

  /* ---------- Hero (header + showcase) ---------- */
  .hero {
    position: absolute; left: 0; top: 0; width: 1132px; height: 582px;
    background: radial-gradient(ellipse 520px 360px at 640px 300px, var(--green-glow) 0%, var(--green-mid) 55%, var(--green-deep) 100%);
    overflow: hidden;
  }
  .site-header {
    position: absolute; left: 0; top: 0; width: 1132px; height: 95px;
    background: linear-gradient(#3f7d18, #468a1c);
    box-shadow: 0 8px 14px -6px rgba(0,0,0,0.35);
  }
  .brand {
    position: absolute; left: 36px; top: 32px;
    display: flex; align-items: center; gap: 10px;
  }
  .brand-dot { width: 22px; height: 22px; border-radius: 50%; background: var(--orange); }
  .brand-name { font-size: 28px; font-weight: 700; color: #2d2d2d; letter-spacing: -0.3px; }

  .main-nav { position: absolute; left: 371px; top: 34px; display: flex; align-items: center; }
  .main-nav a {
    color: var(--white); text-decoration: none; font-size: 15px;
    height: 27px; line-height: 27px; padding: 0 14px; margin-right: 4px;
  }
  .main-nav a.is-active {
    background: linear-gradient(var(--orange-light), var(--orange-dark));
    border-radius: 3px; padding: 0 15px; margin-right: 0;
    box-shadow: 0 2px 3px rgba(0,0,0,0.3);
  }

  .hero-visual {
    position: absolute; left: 33px; top: 229px; width: 474px; height: 256px;
    background: radial-gradient(ellipse at 40% 50%, #e6e9ea 0%, #b9bfc2 40%, rgba(120,170,60,0.6) 70%, rgba(90,160,40,0) 100%);
    border-radius: 40% 45% 40% 45%;
  }
  .hero-copy { position: absolute; left: 516px; top: 330px; }
  .hero-kicker { font-size: 34px; font-weight: 400; color: #2c3a24; line-height: 40px; }
  .hero-title {
    font-size: 36px; font-weight: 700; color: var(--white);
    line-height: 44px; margin-top: 2px;
  }

  .feature-list { position: absolute; left: 896px; top: 121px; width: 203px; }
  .feature-card {
    height: 74px; margin-bottom: 18px; display: flex; align-items: center;
    padding-left: 8px;
    border: 1px solid var(--card-border); border-radius: 3px;
    background: rgba(40,90,10,0.35);
  }
  .feature-card.is-current { border-color: var(--green-accent); background: rgba(40,90,10,0.25); }
  .feature-thumb { width: 75px; height: 57px; flex: none; }
  .feature-text { margin-left: 22px; font-size: 13.5px; line-height: 19px; color: var(--white); }
  .feature-text strong { font-weight: 700; display: block; }
  .feature-card.is-current strong { color: var(--green-accent); }

  /* ---------- Programs band ---------- */
  .programs {
    position: absolute; left: 0; top: 582px; width: 1132px; height: 272px;
    background: var(--grey-band);
  }
  .program { position: absolute; top: 32px; width: 312px; }
  .program h2 { font-size: 27px; font-weight: 400; color: #333; line-height: 34px; }
  .program p { margin-top: 14px; font-size: 13.5px; line-height: 18.5px; color: #2e2e2e; }

  /* ---------- Call to action ---------- */
  .cta { position: absolute; left: 0; top: 854px; width: 1132px; height: 153px; background: var(--white); }
  .cta p { position: absolute; left: 41px; top: 47px; width: 752px; font-size: 13.5px; line-height: 18.5px; color: #2e2e2e; }
  .cta-button {
    position: absolute; left: 808px; top: 47px; width: 263px; height: 54px;
    background: linear-gradient(var(--orange-light), var(--orange) 55%, var(--orange-dark));
    border-radius: 3px; box-shadow: 0 2px 3px rgba(0,0,0,0.3);
    font-size: 23px; line-height: 54px; text-align: center; color: #3a2418;
    text-decoration: none;
  }
  .cta-button b { font-weight: 700; }

  /* ---------- Footer ---------- */
  .site-footer {
    position: absolute; left: 0; top: 1007px; width: 1132px; height: 193px;
    background: var(--footer); color: var(--white); text-align: center;
  }
  .social { position: absolute; left: 493px; top: 47px; display: flex; gap: 9px; }
  .social span { width: 20px; height: 20px; border-radius: 50%; display: block; }
  .social .s1 { background: #1b8fd8; }
  .social .s2 { background: #4d6fae; }
  .social .s3 { background: #e8e8e8; }
  .social .s4 { background: #3fb4e0; }
  .social .s5 { background: #f08a1c; }
  .footer-nav { position: absolute; left: 0; top: 95px; width: 1132px; display: flex; justify-content: center; gap: 28px; }
  .footer-nav a { color: var(--white); text-decoration: none; font-size: 12.5px; }
  .legal { position: absolute; left: 0; top: 136px; width: 1132px; font-size: 11px; line-height: 17px; }
</style>
</head>
<body>

<section class="hero">
  <header class="site-header">
    <div class="brand">
      <span class="brand-dot"></span>
      <span class="brand-name">TravlinFit</span>
    </div>
    <nav class="main-nav">
      <a class="is-active" href="#">Home</a>
      <a href="#">Fitness</a>
      <a href="#">Nutrition</a>
      <a href="#">Fit Lounge</a>
      <a href="#">Fit Score</a>
      <a href="#">Fit School</a>
      <a href="#">Contact Us</a>
      <a href="#">Sign up</a>
    </nav>
  </header>

  <div class="hero-visual" role="img" aria-label="Chrome dumbbell and weight plates beside a green apple"></div>

  <div class="hero-copy">
    <p class="hero-kicker">What We Believe</p>
    <h1 class="hero-title">Motivation, Support<br>and Accountability<br>by Workout</h1>
  </div>

  <div class="feature-list">
    <div class="feature-card">
      <div class="feature-thumb" role="img" aria-label="Man holding a dumbbell and fruit" style="background:linear-gradient(#d9d4cc,#a9a39a);"></div>
      <div class="feature-text"><strong>Lorem Ipsum</strong>is simply</div>
    </div>
    <div class="feature-card is-current">
      <div class="feature-thumb" role="img" aria-label="Dumbbell with a green apple" style="background:linear-gradient(#e4e6e7,#9fa6a8);"></div>
      <div class="feature-text"><strong>Lorem Ipsum</strong>is simply</div>
    </div>
    <div class="feature-card">
      <div class="feature-thumb" role="img" aria-label="Athlete lifting a dumbbell" style="background:linear-gradient(#f2ede8,#b88e70);"></div>
      <div class="feature-text"><strong>Lorem Ipsum</strong>is simply</div>
    </div>
    <div class="feature-card">
      <div class="feature-thumb" role="img" aria-label="Close-up of toned abdominal muscles" style="background:linear-gradient(#c9946f,#8a5a3c);"></div>
      <div class="feature-text"><strong>Lorem Ipsum</strong>is simply</div>
    </div>
    <div class="feature-card">
      <div class="feature-thumb" role="img" aria-label="Woman seated in a yoga pose holding vegetables" style="background:linear-gradient(#f4f4f2,#c9d7b4);"></div>
      <div class="feature-text"><strong>Lorem Ipsum</strong>is simply</div>
    </div>
  </div>
</section>

<section class="programs">
  <article class="program" style="left:45px;">
    <h2>Fit Lounge</h2>
    <p>Lorem Ipsum is simply dummy text of the printing and typesetting industry. Lorem Ipsum has been the industry's standard dummy text ever since the 1500s, when an unknown printer took a galley of type and scrambled it to make a type specimen book. It has survived not only five centuries, but also the leap into electronic typesetting, remaining essentially unchanged.</p>
  </article>
  <article class="program" style="left:413px;">
    <h2>Fit Score</h2>
    <p>Lorem Ipsum is simply dummy text of the printing and typesetting industry. Lorem Ipsum has been the industry's standard dummy text ever since the 1500s, when an unknown printer took a galley of type and scrambled it to make a type specimen book. It has survived not only five centuries, but also the leap into electronic typesetting, remaining essentially unchanged.</p>
  </article>
  <article class="program" style="left:778px;">
    <h2>Fit School</h2>
    <p>Lorem Ipsum is simply dummy text of the printing and typesetting industry. Lorem Ipsum has been the industry's standard dummy text ever since the 1500s, when an unknown printer took a galley of type and scrambled it to make a type specimen book. It has survived not only five centuries, but also the leap into electronic typesetting, remaining essentially unchanged.</p>
  </article>
</section>

<section class="cta">
  <p>Lorem Ipsum is simply dummy text of the printing and typesetting industry. Lorem Ipsum has been the industry's standard dummy text ever since the 1500s, when an unknown printer took a galley of type and scrambled it to make a type specimen book. It has survived not only five centuries, but also the leap into electronic typesetting, remaining essentially</p>
  <a class="cta-button" href="#"><b>Get Started</b> Free Trial</a>
</section>

<footer class="site-footer">
  <div class="social">
    <span class="s1"></span><span class="s2"></span><span class="s3"></span><span class="s4"></span><span class="s5"></span>
  </div>
  <nav class="footer-nav">
    <a href="#">Home</a>
    <a href="#">Fitness</a>
    <a href="#">Nutrition</a>
    <a href="#">Fit Lounge</a>
    <a href="#">Fit Score</a>
    <a href="#">Fit School</a>
    <a href="#">Contact Us</a>
    <a href="#">Sign up</a>
  </nav>
  <div class="legal">
    © 2012 Travlin Fit, All Rights Reserved<br>
    Terms of Service - Privacy Policy - Program Policies
  </div>
</footer>

</body>
</html>
```